New Business Card & Logo Design Project for PR Agency

Halvery & Partners Tech Public Relations agency is looking for a new business card design. Please see our website at www.halvery-pr.example for a description of our services. The design does not necessarily have to match the website’s aesthetic as we are looking for something fresh and modern that reflects our business. We want to emphasize that our focus is on media & public relations, content creation, social media and SEO. We want the business card to convey our BtoB technology focus and should have a very clean look. You are welcome to draw from our current halvery & partners logo on the card or play with that design too. We also like the idea of utilizing blue and white, which are often used in technology-related designs and layouts.
Attached are jpegs of the current logo and current card design for your reference.
Target Market(s)
Our clients are Business-to-Business technology providers.We sell our services to the CEO/President/Marketing director of a technology providing company.
Industry/Entity Type
Business
Look and feel

```html
<!DOCTYPE html>
<html lang="en">
<head>
<meta charset="utf-8">
<title>Halvery &amp; Partners — Business Card</title>
<link href="https://fonts.googleapis.com/css2?family=Roboto+Slab:wght@400;700;900&display=swap" rel="stylesheet">
<style>
  :root {
    --stage: #2b2b2b;
    --card-dark: #222222;
    --card-light: #f4f4f4;
    --ink: #1c1c1c;
    --ink-soft: #333333;
    --accent: #1a9bd7;
    --white: #ffffff;
  }
  * { box-sizing: border-box; margin: 0; padding: 0; }
  html, body {
    width: 1200px; height: 900px; overflow: hidden;
    background: var(--stage);
    font-family: "Roboto Slab", Georgia, serif;
  }
  .stage {
    position: relative; width: 1200px; height: 900px;
    display: flex; align-items: center; justify-content: center; gap: 60px;
  }
  .card {
    position: relative; width: 510px; height: 292px;
    box-shadow: 0 14px 34px rgba(0,0,0,.45);
  }
  .card--front { background: var(--card-dark); }
  .card--back { background: var(--card-light); }

  .wordmark {
    position: absolute;
    font-weight: 900; letter-spacing: -0.5px; line-height: 1;
    white-space: nowrap;
  }
  .card--front .wordmark {
    left: 58px; top: 112px; font-size: 44px; color: var(--white);
  }
  .card--back .wordmark {
    right: 34px; top: 70px; font-size: 32px; color: var(--ink);
  }

  .services {
    position: absolute; left: 58px; top: 198px;
    font-size: 13px; color: var(--accent);
  }
  .services .sep { color: var(--white); margin: 0 5px; }

  .address {
    position: absolute; left: 34px; top: 150px;
    padding-right: 12px; border-right: 1.5px solid var(--accent);
    text-align: right; font-size: 12.5px; line-height: 1.3; color: var(--ink-soft);
  }
  .address .firm { color: var(--accent); }

  .contact {
    position: absolute; right: 30px; top: 158px;
    text-align: right; color: var(--ink-soft);
  }
  .contact .name { font-size: 17px; font-weight: 700; color: var(--accent); }
  .contact .role { font-size: 13px; margin-bottom: 10px; }
  .contact ul { list-style: none; font-size: 12.5px; line-height: 1.45; }
  .contact li { display: flex; align-items: center; justify-content: flex-end; gap: 6px; }
  .contact svg { width: 11px; height: 11px; flex: none; }
</style>
</head>
<body>
  <main class="stage">
    <section class="card card--front" aria-label="Card front">
      <div class="wordmark">halvery &amp; partners</div>
      <p class="services">High Tech PR<span class="sep">|</span>Web Content<span class="sep">|</span>Social Media<span class="sep">|</span>SEO</p>
    </section>

    <section class="card card--back" aria-label="Card back">
      <div class="wordmark">halvery &amp; partners</div>
      <address class="address">
        <span class="firm">Halvery &amp; Partners</span><br>
        48 Harbor Lane, Suite 2<br>
        Linwood, Vermont 05012
      </address>
      <div class="contact">
        <p class="name">Celia Halvery</p>
        <p class="role">Principal</p>
        <ul>
          <li>(555) 014-2871
            <svg viewBox="0 0 12 12"><circle cx="6" cy="6" r="6" fill="#1a9bd7"/><path d="M4 3.2l1 1.6-.6.6a4 4 0 0 0 2.2 2.2l.6-.6 1.6 1-.6 1A5 5 0 0 1 3 4z" fill="#fff"/></svg>
          </li>
          <li>chalvery@halvery-pr.example
            <svg viewBox="0 0 12 12"><circle cx="6" cy="6" r="6" fill="#1a9bd7"/><rect x="3" y="4" width="6" height="4.2" fill="none" stroke="#fff" stroke-width=".9"/><path d="M3 4l3 2.3L9 4" fill="none" stroke="#fff" stroke-width=".9"/></svg>
          </li>
          <li>www.halvery-pr.example
            <svg viewBox="0 0 12 12"><circle cx="6" cy="6" r="6" fill="#1a9bd7"/><circle cx="6" cy="6" r="3" fill="none" stroke="#fff" stroke-width=".9"/><path d="M3 6h6M6 3v6" stroke="#fff" stroke-width=".7"/></svg>
          </li>
        </ul>
      </div>
    </section>
  </main>
</body>
</html>
```